Corporate Design für Handel mit Schützenausrüstung
Es war eine hervorragende Zusammenarbeit mit Firebird, sie ist sehr freundliche, hilfsbereit und hat tolle Ideen. Sie hat meine Wünsche sofort und absolut professionell umgesetzt. So konnten wir sehr schnell das perfekte Logo für mich finden. Ich kann Firebird nur absolut empfehlen. Vielen Dank!
Zielgruppe
Ich bin Inhaber von einem neu gegründeten Einzelunternehmen und möchte mit Waffen, Munition, Schützenausrüstung und Selbstschutzartikeln handeln.
Ich benötigte ein ansprechendes Corporate-Design mit einem thematisch passenden Logo.
Meine Zielgruppe sind Sportschützen (m/w) und Jäger (m/w) im Alter von 30-70 Jahren.
Aufgabenstellung
Das Corporate-Design sollte für die Kunden möglichst klar auf die Unternehmenstätigkeit hinweisen und Zuverlässigkeit und Dynamik vermittelt.
Da der Handel mit Munition den größten Teil ausmacht, sollte dieses auch im Mittelpunkt des Logos stehen. Allerdings sollte auch ein Bezug zu den Waffen nicht fehlen.
Meine Vorstellung wäre ein Schild auf dem eine Patrone / Geschoss abgebildet ist und von Waffen flankiert wird.
Ideal wäre daher ein Logo im Wappen-Stiel.
Von den Farben her habe ich noch keine konkreten Vorstellungen. Vielleicht wäre blau nicht schlecht, als Anspielung auf 'blaue Bohnen'.

```html
<!DOCTYPE html>
<html lang="de">
<head>
<meta charset="utf-8">
<title>Schützenbedarf Jonas Brenning – Geschäftsausstattung</title>
<link href="https://fonts.googleapis.com/css2?family=Open+Sans:wght@400;600;700&display=swap" rel="stylesheet">
<style>
  :root {
    --ink: #1c2d35;
    --sage: #a8a89a;
    --paper: #f6f6f3;
    --text: #1f1f1f;
    --muted: #5a5a5a;
    --backdrop: #6a6a68;
  }
  * { margin: 0; padding: 0; box-sizing: border-box; }
  html, body { width: 1200px; height: 977px; overflow: hidden; }
  body {
    background: var(--backdrop);
    font-family: "Open Sans", sans-serif;
    color: var(--text);
    position: relative;
  }
  .sheet { position: absolute; background: var(--paper); overflow: hidden; }
  .corner { position: absolute; left: 0; top: 0; display: block; }

  .brand-name {
    font-family: "Open Sans", sans-serif;
    font-weight: 700;
    color: var(--ink);
    text-align: center;
    text-transform: uppercase;
    line-height: 1.15;
    display: flex;
    flex-direction: column;
    align-items: center;
    gap: 4px;
    white-space: nowrap;
  }
  .brand-name .dot {
    width: 8px; height: 8px; border-radius: 50%; background: var(--ink);
  }

  /* Visitenkarte Vorderseite */
  .card-front { left: 114px; top: 249px; width: 177px; height: 119px;
    display: flex; align-items: center; justify-content: center; }
  .card-front .brand-name { font-size: 11px; }

  /* Visitenkarte Rückseite */
  .card-back { left: 114px; top: 378px; width: 179px; height: 119px; }
  .card-back .holder { position: absolute; left: 13px; top: 11px;
    font-size: 8px; font-weight: 700; }
  .card-back .details { position: absolute; left: 14px; top: 31px;
    font-size: 5.4px; line-height: 1.5; }
  .card-back .details .gap { margin-top: 2px; }
  .card-back .brand-name { position: absolute; right: 12px; bottom: 22px;
    font-size: 5.5px; }
  .card-back .brand-name .dot { width: 5px; height: 5px; }

  /* Briefbogen */
  .letterhead { left: 353px; top: 228px; width: 286px; height: 402px; }
  .letterhead .brand-name { position: absolute; right: 22px; top: 26px;
    font-size: 7.5px; }
  .letterhead .fold-mark { position: absolute; left: 0; width: 12px;
    height: 1px; background: #c9c9c4; }
  .letterhead .footer-col { position: absolute; top: 373px;
    font-size: 4px; line-height: 1.45; color: var(--muted); white-space: nowrap; }
  .letterhead .footer-col strong { color: var(--text); font-weight: 600; }
  .letterhead .col-sender  { left: 40px; }
  .letterhead .col-contact { left: 89px; }
  .letterhead .col-tax     { left: 167px; }
  .letterhead .col-bank    { left: 224px; }

  /* Briefumschlag */
  .envelope { left: 792px; top: 309px; width: 331px; height: 197px; background: #fbfbfa; }
  .envelope .brand-name { position: absolute; left: 16px; top: 56px;
    font-size: 5.5px; }
  .envelope .brand-name .dot { width: 5px; height: 5px; }
</style>
</head>
<body>

  <section class="sheet card-front" aria-label="Visitenkarte Vorderseite">
    <div class="brand-name">Schützenbedarf<br>Jonas Brenning<span class="dot"></span></div>
  </section>

  <section class="sheet card-back" aria-label="Visitenkarte Rückseite">
    <svg class="corner" width="179" height="119" viewBox="0 0 179 119" aria-hidden="true">
      <path d="M120 0 C148 8 168 22 179 40 L179 0 Z" fill="var(--sage)"/>
      <path d="M138 0 C158 9 172 20 179 32 L179 0 Z" fill="var(--ink)"/>
      <path d="M0 78 C10 102 30 116 58 119 L0 119 Z" fill="var(--sage)"/>
      <path d="M0 86 C8 104 20 115 36 119 L0 119 Z" fill="var(--ink)"/>
    </svg>
    <div class="holder">JONAS BRENNING</div>
    <div class="details">
      Lindenweg 7<br>34567 Beispielstadt
      <div class="gap">+49 171 5550 4821</div>
      <div class="gap">email@schuetzenbedarf-brenning.com<br>www.schuetzenbedarf-brenning.com</div>
    </div>
    <div class="brand-name">Schützenbedarf<br>Jonas Brenning<span class="dot"></span></div>
  </section>

  <section class="sheet letterhead" aria-label="Briefbogen">
    <svg class="corner" width="286" height="402" viewBox="0 0 286 402" aria-hidden="true">
      <path d="M244 0 C266 10 281 28 286 52 L286 0 Z" fill="var(--sage)"/>
      <path d="M260 0 C275 9 284 22 286 36 L286 0 Z" fill="var(--ink)"/>
      <path d="M0 350 C5 380 22 398 48 402 L0 402 Z" fill="var(--sage)"/>
      <path d="M0 362 C3 384 14 398 30 402 L0 402 Z" fill="var(--ink)"/>
    </svg>
    <div class="brand-name">Schützenbedarf<br>Jonas Brenning<span class="dot"></span></div>
    <span class="fold-mark" style="top:131px"></span>
    <span class="fold-mark" style="top:270px"></span>
    <div class="footer-col col-sender"><strong>Jonas Brenning</strong><br>Lindenweg 7<br>34567 Beispielstadt</div>
    <div class="footer-col col-contact">Tel.: +49 176 5550 1234<br>email@schuetzenbedarf-brenning.com<br>www.schuetzenbedarf-brenning.com</div>
    <div class="footer-col col-tax">Steuernr.: 4411098877<br>Stadtbank</div>
    <div class="footer-col col-bank">IBAN: DE00 1234 5678 9012<br>BIC: STDBDEXX000</div>
  </section>

  <section class="sheet envelope" aria-label="Briefumschlag">
    <div class="brand-name">Schützenbedarf<br>Jonas Brenning<span class="dot"></span></div>
  </section>

</body>
</html>
```